International Honeymoon Tour Operator needs Business Card

We need to design a business card including our new logo for a new tour operator called Marisol Thorne Getaways. We would like to also include the text 'Personal Tailor-Made Honeymoons for our Guests at a Lower Cost'. Please Include the following details as well; 'Website: www.marisolthornegetaways.co.uk'; 'E-mail: felix@marisolthornegetaways.co.uk'; 'Mobile: 07914263058'. We would like the design to be compatible with the logo and text. The final design should communicate professionalism, modern and ethical.

We want to business card to be double sided.

We would like to be able to easily adjust the e-mail address and contact number in the future for other employees either through you or ourselves.

Target Market(s)

Brides and grooms aged 18-35 predominantly.

Industry/Entity Type

Business

Colors

Designer to choose colors to be used in the design.

Requirements
Must have
• Logo
Requested Text
Double sided
Nice to have
• Additional colour
The wow factor
Should not have
• Images of currency

```html
<!DOCTYPE html>
<html lang="en">
<head>
<meta charset="utf-8">
<title>Marisol Thorne Getaways – Business Card</title>
<link href="https://fonts.googleapis.com/css2?family=Questrial&family=Montserrat:wght@600&display=swap" rel="stylesheet">
<style>
  :root {
    --backdrop: #6f6c6b;
    --card-white: #f4f4f2;
    --teal: #4f7b6d;
    --teal-band: #5b8676;
    --lime: #c8dc6e;
    --leaf: #8dbb4a;
    --ink-light: #ffffff;
    --ink-soft: #e3ece8;
  }
  * { margin: 0; padding: 0; box-sizing: border-box; }
  html, body {
    width: 1200px; height: 799px; overflow: hidden;
    background: var(--backdrop);
    font-family: "Questrial", sans-serif;
  }
  .stage { position: relative; width: 1200px; height: 799px; }

  .card { position: absolute; left: 380px; width: 440px; }

  /* Front */
  .card-front {
    top: 79px; height: 273px;
    background: var(--card-white);
  }
  .brand-front {
    position: absolute; left: 0; right: 0; top: 132px;
    display: flex; align-items: center; justify-content: center; gap: 10px;
  }
  .brand-dot {
    width: 14px; height: 14px; border-radius: 50%;
    background: var(--leaf);
  }
  .brand-name-front {
    font-size: 29px; color: var(--teal); letter-spacing: 0.3px;
  }
  .tagline-band {
    position: absolute; left: 0; right: 0; top: 222px; height: 21px;
    background: var(--teal-band);
    display: flex; align-items: center; justify-content: center;
  }
  .tagline {
    font-family: "Montserrat", sans-serif; font-weight: 600;
    font-size: 8.6px; letter-spacing: 0.6px; text-transform: uppercase;
    color: var(--lime);
  }

  /* Back */
  .card-back {
    top: 444px; height: 262px;
    background: var(--teal);
  }
  .brand-name-back {
    position: absolute; left: 46px; top: 50px;
    font-size: 22px; color: var(--ink-light);
  }
  .holder { position: absolute; left: 46px; top: 154px; color: var(--ink-light); }
  .holder-name {
    font-family: "Montserrat", sans-serif; font-weight: 600;
    font-size: 11.5px; letter-spacing: 1px; text-transform: uppercase;
  }
  .holder-role {
    font-family: "Montserrat", sans-serif; font-weight: 600;
    font-size: 8.5px; letter-spacing: 0.8px; margin-top: 4px;
  }
  .contact {
    position: absolute; left: 46px; top: 195px;
    list-style: none; color: var(--ink-soft);
    font-size: 6.4px; letter-spacing: 0.5px; text-transform: uppercase;
    line-height: 14.5px;
  }
</style>
</head>
<body>
<main class="stage">
  <section class="card card-front" aria-label="Business card front">
    <div class="brand-front">
      <span class="brand-dot"></span>
      <span class="brand-name-front">Marisol Thorne Getaways</span>
    </div>
    <div class="tagline-band">
      <p class="tagline">Personal tailor-made honeymoons for our guests at a lower cost</p>
    </div>
  </section>

  <section class="card card-back" aria-label="Business card back">
    <p class="brand-name-back">Marisol Thorne Getaways</p>
    <div class="holder">
      <p class="holder-name">Reza Holm</p>
      <p class="holder-role">CEO</p>
    </div>
    <ul class="contact">
      <li class="contact-web">www.marisolthornegetaways.co.uk</li>
      <li class="contact-email">felix@marisolthornegetaways.co.uk</li>
      <li class="contact-phone">07914263058</li>
    </ul>
  </section>
</main>
</body>
</html>
```